Plate Bright Workshop (workshop to teach people to eat fruits and vegetables)

Double sided DL Flyer

Free Community Workshop
Plate Bright Live Lively
Central Coast NSW

Copy to appear on flyer side one:-
PLATE BRIGHT LIVE LIVELY
interactive workshops
March-April 2019
Presented by qualified nutritionist

Food for healthier happier life for you and your family (free to central coast residents - all ages welcome

Side 2
Learn About:-
Foods that improve your health
basic nutrition
gut brain connection
portion size
menu planning
preparation
eating

Benefits
Improved health
Improved Energy
Manage chronic illness
diabetes type II
cholesterol
Blood Pressure
Family fun

Food Tastings
Lucky Door Prize

Reserve for spot online @ www.platebright.com.au or call 0462 508 731
Supported by Harbourline Shire Council (Logo) Harbourline Rugby Social Club (Logo) Pindara Veterans Club (Logo)

I would like to see a flyer that is bright, fun and fresh with images of fresh food.

Target Market(s)

Women 30 plus

Industry/Entity Type

Health And Wellness

Logo Text

PLATE BRIGHT LIVE LIVELY

Font styles to use
Other font styles liked:
• bold clean

Colors
f37122
9bcb3c
fbed22
ec1f27
e34297

Requirements
Must have
• bright eye catching colours featuring fresh fruit and vegetables
• I have attached a some images of designs I like
Nice to have
• Im happy for the designer to change copy to create a clean flyer without loosing essential information
• I like the feel of the banner on my facebook page
• Kindly Nourish - Plate Bright Live Lively with Megan Troute
• https://www.facebook.com/kindlynourishoz/
Should not have
• old fashioned images

```html
<!DOCTYPE html>
<html lang="en">
<head>
<meta charset="utf-8">
<title>Kindly Nourish – Plate Bright Workshop DL Flyer</title>
<link href="https://fonts.googleapis.com/css2?family=Bebas+Neue&family=Catamaran:wght@300;400;600&family=Open+Sans:ital,wght@1,400&display=swap" rel="stylesheet">
<style>
  :root{
    --pink:#e0197f;
    --pink-dark:#b5126a;
    --green:#8cc63f;
    --yellow:#f7c51e;
    --ink:#3c3c3c;
    --paper:#efefef;
    --stage:#e4e4e4;
    --white:#ffffff;
  }
  *{box-sizing:border-box;margin:0;padding:0}
  html,body{width:1199px;height:1200px;overflow:hidden;background:var(--stage)}
  .canvas{position:relative;width:1199px;height:1200px}
  .flyer{position:absolute;top:104px;width:471px;height:988px;overflow:hidden;
    background:linear-gradient(180deg,#f6f6f6,var(--paper));
    box-shadow:0 4px 14px rgba(0,0,0,.18);font-family:"Catamaran",sans-serif;color:var(--ink)}
  .flyer--front{left:97px}
  .flyer--back{left:634px}
  .abs{position:absolute}
  .shapes{position:absolute;inset:0;width:471px;height:988px}
  .photo{position:absolute}
  .badge{position:absolute;border-radius:50%;display:flex;align-items:center;justify-content:center;
    text-align:center;font-family:"Bebas Neue",sans-serif;color:var(--white);line-height:.92}
  .badge--free{left:280px;top:198px;width:184px;height:184px;background:var(--yellow);
    border:6px solid var(--white);box-shadow:0 0 0 3px var(--yellow)}
  .badge--free .big{font-size:54px;display:block}
  .badge--free .small{font-size:30px;display:block}
  .badge--tastings{left:29px;top:187px;width:170px;height:170px;background:var(--green);
    border:6px solid var(--white);box-shadow:0 0 0 3px var(--green);font-size:30px}
  .brand{position:absolute;display:flex;align-items:center;gap:12px;
    font-family:"Bebas Neue",sans-serif;color:var(--pink);font-size:46px;line-height:.9}
  .brand__dot{width:22px;height:22px;border-radius:50%;background:var(--pink);flex:none}
  .tab{position:absolute;background:var(--pink);color:var(--white);font-family:"Bebas Neue",sans-serif}
  .tab--headline{left:0;top:445px;width:398px;height:50px;border-radius:0 25px 25px 0;
    font-size:40px;line-height:52px;padding-left:29px}
  .tab--learn{left:0;top:372px;width:218px;height:36px;border-radius:0 18px 18px 0;
    font-size:29px;line-height:38px;padding-left:31px}
  .tab--benefits{left:274px;top:550px;width:197px;height:36px;border-radius:18px 0 0 18px;
    font-size:29px;line-height:38px;padding-left:52px}
  .checks{position:absolute;left:31px;top:510px;list-style:none;font-size:24px;font-weight:300;line-height:33px}
  .checks li{display:flex;align-items:center;gap:9px}
  .tick{width:18px;height:18px;flex:none}
  .tagline{position:absolute;left:245px;top:671px;font-family:"Open Sans",sans-serif;font-style:italic;
    color:var(--green);font-size:17px;line-height:24px}
  .learn{position:absolute;left:33px;top:428px;list-style:none;font-size:21px;font-weight:300;line-height:28.2px}
  .learn li,.benefits li,.contact li{display:flex;align-items:center;gap:10px}
  .chev{width:15px;height:15px;flex:none}
  .sun{position:absolute;left:176px;top:492px;width:340px;height:340px;border-radius:50%;background:var(--yellow);
    box-shadow:0 0 0 6px rgba(255,255,255,.8)}
  .benefits{position:absolute;right:17px;top:596px;list-style:none;color:var(--white);font-size:21px;
    font-weight:400;line-height:28.2px;text-align:right}
  .benefits li{justify-content:flex-end}
  .supported{position:absolute;left:25px;top:666px;font-family:"Open Sans",sans-serif;font-style:italic;
    color:var(--green);font-size:17px}
  .partners{position:absolute;left:25px;top:708px;display:flex;align-items:center;gap:12px}
  .partner{background:#1d3e6e}
  .partner--wide{width:62px;height:34px;border-radius:6px;background:#d9e3ee}
  .partner--round{width:40px;height:40px;border-radius:50%}
  .partner--crest{width:66px;height:38px;border-radius:8px}
  .reserve{position:absolute;top:864px;font-family:"Bebas Neue",sans-serif;color:var(--yellow);font-size:25px}
  .contact{position:absolute;top:900px;list-style:none;font-size:18px;font-weight:400;line-height:26.5px}
  .flyer--front .reserve{right:21px}
  .flyer--front .contact{right:21px}
  .flyer--front .contact li{justify-content:flex-end}
  .flyer--back .reserve{left:28px}
  .flyer--back .contact{left:26px}
  .ico{width:19px;height:19px;flex:none}
</style>
</head>
<body>
<main class="canvas">

  <!-- Side one -->
  <section class="flyer flyer--front">
    <div class="photo" role="img" aria-label="Overhead photo of fresh fruit, vegetables, grains and berries in heart-shaped bowls"
      style="left:0;top:0;width:471px;height:290px;background:linear-gradient(135deg,#c9452c,#e68a2e 35%,#6f8f3a 60%,#f2c94c);
      clip-path:path('M0,0 H471 V190 C330,268 150,286 0,226 Z')"></div>
    <svg class="shapes" viewBox="0 0 471 988" aria-hidden="true">
      <path d="M0,226 C150,286 330,268 471,190 L471,214 C330,296 150,312 0,258 Z" fill="var(--pink)"/>
      <path d="M0,258 C150,312 330,296 471,214 L471,226 C330,306 150,322 0,270 Z" fill="var(--green)"/>
      <path d="M0,842 C150,770 320,752 471,772 L471,988 L0,988 Z" fill="var(--green)"/>
      <path d="M0,856 C150,790 320,776 471,790 L471,988 L0,988 Z" fill="var(--pink)"/>
      <path d="M118,988 C140,900 270,842 471,838 L471,950 C462,968 455,978 446,988 Z" fill="var(--white)"/>
    </svg>

    <div class="badge badge--free"><div><span class="big">Free</span><span class="small">Community<br>Workshop</span></div></div>

    <div class="brand" style="left:30px;top:330px">Kindly<br>Nourish<span class="brand__dot"></span></div>

    <h1 class="tab tab--headline">PLATE BRIGHT LIVE LIVELY</h1>

    <ul class="checks">
      <li><svg class="tick" viewBox="0 0 20 20"><circle cx="10" cy="10" r="8.5" fill="none" stroke="var(--pink)" stroke-width="2"/><path d="M6 10.5l3 3 6-7" fill="none" stroke="var(--pink)" stroke-width="2.2"/></svg>Interactive Workshops</li>
      <li><svg class="tick" viewBox="0 0 20 20"><circle cx="10" cy="10" r="8.5" fill="none" stroke="var(--pink)" stroke-width="2"/><path d="M6 10.5l3 3 6-7" fill="none" stroke="var(--pink)" stroke-width="2.2"/></svg>March-April 2019</li>
      <li><svg class="tick" viewBox="0 0 20 20"><circle cx="10" cy="10" r="8.5" fill="none" stroke="var(--pink)" stroke-width="2"/><path d="M6 10.5l3 3 6-7" fill="none" stroke="var(--pink)" stroke-width="2.2"/></svg>Presented By Qualified Nutritionist</li>
    </ul>

    <div class="photo" role="img" aria-label="Glasses of colourful fresh juice with sliced citrus fruit"
      style="left:0;top:616px;width:240px;height:240px;border-radius:0 40px 0 0;
      background:linear-gradient(90deg,#9cc94a,#e8504a 35%,#f7a531 60%,#f3d34a)"></div>

    <p class="tagline">Food for healthier happier<br>life for you and your family<br>all ages welcome</p>

    <p class="reserve">Reserve for spot online</p>
    <ul class="contact">
      <li>0462 508 731<svg class="ico" viewBox="0 0 20 20"><circle cx="10" cy="10" r="9" fill="var(--yellow)"/><path d="M7 5.5l2 2-1 1.5c.8 1.6 1.9 2.7 3.5 3.5l1.5-1 2 2-1.5 1.5C9.5 15 5 10.5 5.5 7z" fill="var(--white)"/></svg></li>
      <li>megan@kindlynourish.com.au<svg class="ico" viewBox="0 0 20 20"><circle cx="10" cy="10" r="9" fill="var(--yellow)"/><rect x="5" y="6.5" width="10" height="7" rx="1" fill="var(--white)"/><path d="M5 7l5 3.5L15 7" fill="none" stroke="var(--yellow)" stroke-width="1.2"/></svg></li>
      <li>www.platebright.com.au<svg class="ico" viewBox="0 0 20 20"><circle cx="10" cy="10" r="9" fill="var(--yellow)"/><circle cx="10" cy="10" r="5.5" fill="none" stroke="var(--white)" stroke-width="1.3"/><path d="M4.5 10h11M10 4.5c-3 3-3 8 0 11M10 4.5c3 3 3 8 0 11" fill="none" stroke="var(--white)" stroke-width="1.1"/></svg></li>
    </ul>
  </section>

  <!-- Side two -->
  <section class="flyer flyer--back">
    <div class="photo" role="img" aria-label="Smiling woman eating a fresh salad"
      style="left:226px;top:0;width:245px;height:300px;background:linear-gradient(160deg,#e9c6a8,#c98f6e 45%,#d43f86 75%,#6e8f3a);
      clip-path:path('M0,0 H245 V200 C180,250 90,270 0,275 Z')"></div>
    <div class="photo" role="img" aria-label="The words eat right spelled out in fruit and vegetables"
      style="left:24px;top:30px;width:210px;height:140px;border-radius:12px;
      background:linear-gradient(120deg,#e04b2f,#f2a63a 40%,#7fb23e 70%,#c33a6a)"></div>
    <svg class="shapes" viewBox="0 0 471 988" aria-hidden="true">
      <path d="M0,226 C120,262 170,270 226,275 C320,268 400,236 471,200 L471,222 C400,262 320,292 226,296 C150,294 80,284 0,262 Z" fill="var(--green)"/>
      <path d="M0,262 C80,284 150,294 226,296 C320,292 400,262 471,222 L471,246 C400,290 320,316 226,318 C150,316 80,306 0,290 Z" fill="var(--pink)"/>
      <path d="M0,790 C150,770 320,790 471,842 L471,988 L0,988 Z" fill="var(--green)"/>
      <path d="M0,806 C150,788 320,806 471,856 L471,988 L0,988 Z" fill="var(--pink)"/>
      <path d="M0,838 C170,836 320,880 354,988 L26,988 C15,978 8,968 0,955 Z" fill="var(--white)"/>
    </svg>

    <div class="badge badge--tastings"><div>Food<br>Tastings<br>Lucky Door<br>Prize</div></div>

    <h2 class="tab tab--learn">Learn About:</h2>
    <div class="brand" style="left:238px;top:344px">Kindly<br>Nourish<span class="brand__dot"></span></div>

    <ul class="learn">
      <li><svg class="chev" viewBox="0 0 16 16"><circle cx="8" cy="8" r="8" fill="var(--yellow)"/><path d="M6.5 4.5L10 8l-3.5 3.5" fill="none" stroke="var(--white)" stroke-width="2"/></svg>Foods That Improve Your Health</li>
      <li><svg class="chev" viewBox="0 0 16 16"><circle cx="8" cy="8" r="8" fill="var(--yellow)"/><path d="M6.5 4.5L10 8l-3.5 3.5" fill="none" stroke="var(--white)" stroke-width="2"/></svg>Basic Nutrition</li>
      <li><svg class="chev" viewBox="0 0 16 16"><circle cx="8" cy="8" r="8" fill="var(--yellow)"/><path d="M6.5 4.5L10 8l-3.5 3.5" fill="none" stroke="var(--white)" stroke-width="2"/></svg>Gut Brain Connection</li>
      <li><svg class="chev" viewBox="0 0 16 16"><circle cx="8" cy="8" r="8" fill="var(--yellow)"/><path d="M6.5 4.5L10 8l-3.5 3.5" fill="none" stroke="var(--white)" stroke-width="2"/></svg>Portion Size</li>
      <li><svg class="chev" viewBox="0 0 16 16"><circle cx="8" cy="8" r="8" fill="var(--yellow)"/><path d="M6.5 4.5L10 8l-3.5 3.5" fill="none" stroke="var(--white)" stroke-width="2"/></svg>Menu Planning</li>
      <li><svg class="chev" viewBox="0 0 16 16"><circle cx="8" cy="8" r="8" fill="var(--yellow)"/><path d="M6.5 4.5L10 8l-3.5 3.5" fill="none" stroke="var(--white)" stroke-width="2"/></svg>Preparation</li>
      <li><svg class="chev" viewBox="0 0 16 16"><circle cx="8" cy="8" r="8" fill="var(--yellow)"/><path d="M6.5 4.5L10 8l-3.5 3.5" fill="none" stroke="var(--white)" stroke-width="2"/></svg>Eating</li>
    </ul>

    <div class="sun"></div>
    <h2 class="tab tab--benefits">Benefits</h2>
    <ul class="benefits">
      <li>Improved Health<svg class="chev" viewBox="0 0 16 16"><circle cx="8" cy="8" r="8" fill="var(--pink)"/><path d="M9.5 4.5L6 8l3.5 3.5" fill="none" stroke="var(--white)" stroke-width="2"/></svg></li>
      <li>Improved Energy<svg class="chev" viewBox="0 0 16 16"><circle cx="8" cy="8" r="8" fill="var(--pink)"/><path d="M9.5 4.5L6 8l3.5 3.5" fill="none" stroke="var(--white)" stroke-width="2"/></svg></li>
      <li>Manage Chronic Illness<svg class="chev" viewBox="0 0 16 16"><circle cx="8" cy="8" r="8" fill="var(--pink)"/><path d="M9.5 4.5L6 8l3.5 3.5" fill="none" stroke="var(--white)" stroke-width="2"/></svg></li>
      <li>Diabetes Type II<svg class="chev" viewBox="0 0 16 16"><circle cx="8" cy="8" r="8" fill="var(--pink)"/><path d="M9.5 4.5L6 8l3.5 3.5" fill="none" stroke="var(--white)" stroke-width="2"/></svg></li>
      <li>Cholesterol<svg class="chev" viewBox="0 0 16 16"><circle cx="8" cy="8" r="8" fill="var(--pink)"/><path d="M9.5 4.5L6 8l3.5 3.5" fill="none" stroke="var(--white)" stroke-width="2"/></svg></li>
      <li>Blood Pressure<svg class="chev" viewBox="0 0 16 16"><circle cx="8" cy="8" r="8" fill="var(--pink)"/><path d="M9.5 4.5L6 8l3.5 3.5" fill="none" stroke="var(--white)" stroke-width="2"/></svg></li>
      <li>Family Fun<svg class="chev" viewBox="0 0 16 16"><circle cx="8" cy="8" r="8" fill="var(--pink)"/><path d="M9.5 4.5L6 8l3.5 3.5" fill="none" stroke="var(--white)" stroke-width="2"/></svg></li>
    </ul>

    <p class="supported">Supported by:</p>
    <div class="partners">
      <div class="partner partner--wide" role="img" aria-label="Harbourline Rugby Social Club badge"></div>
      <div class="partner partner--round" role="img" aria-label="Harbourline Shire Council badge"></div>
      <div class="partner partner--crest" role="img" aria-label="Pindara Veterans Club badge"></div>
    </div>

    <p class="reserve">Reserve for spot online</p>
    <ul class="contact">
      <li><svg class="ico" viewBox="0 0 20 20"><circle cx="10" cy="10" r="9" fill="var(--yellow)"/><path d="M7 5.5l2 2-1 1.5c.8 1.6 1.9 2.7 3.5 3.5l1.5-1 2 2-1.5 1.5C9.5 15 5 10.5 5.5 7z" fill="var(--white)"/></svg>0462 508 731</li>
      <li><svg class="ico" viewBox="0 0 20 20"><circle cx="10" cy="10" r="9" fill="var(--yellow)"/><rect x="5" y="6.5" width="10" height="7" rx="1" fill="var(--white)"/><path d="M5 7l5 3.5L15 7" fill="none" stroke="var(--yellow)" stroke-width="1.2"/></svg>megan@kindlynourish.com.au</li>
      <li><svg class="ico" viewBox="0 0 20 20"><circle cx="10" cy="10" r="9" fill="var(--yellow)"/><circle cx="10" cy="10" r="5.5" fill="none" stroke="var(--white)" stroke-width="1.3"/><path d="M4.5 10h11M10 4.5c-3 3-3 8 0 11M10 4.5c3 3 3 8 0 11" fill="none" stroke="var(--white)" stroke-width="1.1"/></svg>www.platebright.com.au</li>
    </ul>
  </section>

</main>
</body>
</html>
```